Cobalto Regal

I want a glossy card on both sides. We sell underwater LED lights for water craft

we sell custom audio enclosures for automobile, boats and atv's.

view our websites for any other pictures you may think are better suited.

Industry/Entity Type

Audio

Contact Information for Business Card

Email address: CobaltoRegal@mailbarn.net
Website: www.hullglowcap.com
underwater LED lighting for watercraft
boat drain plug lights
phone number: 555-271-6048

other side of card:
email address the same
website: www.versatilesoundshells.com
speaker enclosures, auto, boat and atv
same phone number

```html
<!DOCTYPE html>
<html lang="en">
<head>
<meta charset="utf-8">
<title>Cobalto Regal – Business Card</title>
<link href="https://fonts.googleapis.com/css2?family=Montserrat:wght@500;600;800&display=swap" rel="stylesheet">
<style>
  :root {
    --paper: #ebebeb;
    --ink: #111111;
    --night: #050505;
    --band: #ffffff;
    --logo-ice: #cfe8ff;
    --photo-deep: #1a1f6e;
    --photo-mid: #3b4fd8;
    --photo-glow: #8fd2ff;
    --photo-violet: #8a5fc8;
  }
  html, body {
    margin: 0;
    padding: 0;
    overflow: hidden;
    background: var(--paper);
  }
  .card {
    position: relative;
    width: 1200px;
    height: 720px;
    background: var(--paper);
    overflow: hidden;
    font-family: "Montserrat", Arial, sans-serif;
    color: var(--ink);
  }
  .card-shapes {
    position: absolute;
    inset: 0;
    width: 1200px;
    height: 720px;
  }
  .brand-name {
    position: absolute;
    left: 88px;
    top: 186px;
    margin: 0;
    font-weight: 600;
    font-size: 64px;
    letter-spacing: 10px;
    color: var(--logo-ice);
    line-height: 1;
  }
  .web-address {
    position: absolute;
    left: 80px;
    top: 356px;
    margin: 0;
    font-weight: 800;
    font-size: 45px;
    line-height: 1;
    letter-spacing: -0.3px;
  }
  .services {
    position: absolute;
    left: 81px;
    top: 422px;
    margin: 0;
    font-weight: 500;
    font-size: 20.5px;
    line-height: 1;
  }
  .contact {
    position: absolute;
    left: 912px;
    top: 555px;
    width: 400px;
    transform: rotate(-52deg);
    transform-origin: 0 100%;
  }
  .contact-email {
    display: flex;
    align-items: center;
    gap: 8px;
    font-weight: 500;
    font-size: 21px;
    line-height: 1;
    margin: 0 0 8px 0;
  }
  .contact-email svg {
    width: 24px;
    height: 18px;
  }
  .contact-phone {
    font-weight: 600;
    font-size: 38px;
    line-height: 1;
    margin: 0 0 0 48px;
    letter-spacing: 0.5px;
  }
</style>
</head>
<body>
<div class="card">
  <svg class="card-shapes" viewBox="0 0 1125 675" preserveAspectRatio="none" aria-hidden="false">
    <defs>
      <linearGradient id="showroom-tone" x1="0" y1="0" x2="1" y2="1">
        <stop offset="0" stop-color="var(--photo-deep)"/>
        <stop offset="0.35" stop-color="var(--photo-mid)"/>
        <stop offset="0.6" stop-color="var(--photo-glow)"/>
        <stop offset="0.8" stop-color="var(--photo-violet)"/>
        <stop offset="1" stop-color="var(--photo-deep)"/>
      </linearGradient>
    </defs>
    <polygon class="dark-chevron" points="0,0 330,0 475,215 140,675 0,675" fill="var(--night)"/>
    <polygon class="showroom-photo-top" role="img" aria-label="Showroom wall of car audio speakers and head units lit with blue LED light"
             points="330,0 930,0 1070,210 1000,315 402,315 475,215" fill="url(#showroom-tone)"/>
    <polygon class="showroom-photo-bottom" role="img" aria-label="Showroom display of speaker enclosures and amplifiers under blue lighting"
             points="317,432 922,432 760,675 140,675" fill="url(#showroom-tone)"/>
    <polygon class="title-band" points="0,315 1000,315 922,432 0,432" fill="var(--band)"/>
  </svg>

  <p class="brand-name">COBALTO</p>
  <h1 class="web-address">WWW.VERSATILESOUNDSHELLS.COM</h1>
  <p class="services">SPEAKER ENCLOSURES, AUTO, BOAT AND ATV</p>

  <div class="contact">
    <p class="contact-email">
      <svg viewBox="0 0 24 18" aria-hidden="true">
        <rect x="1" y="1" width="22" height="16" fill="none" stroke="var(--ink)" stroke-width="1.5"/>
        <polyline points="1,1 12,10 23,1" fill="none" stroke="var(--ink)" stroke-width="1.5"/>
        <line x1="1" y1="17" x2="9" y2="8" stroke="var(--ink)" stroke-width="1.2"/>
        <line x1="23" y1="17" x2="15" y2="8" stroke="var(--ink)" stroke-width="1.2"/>
      </svg>
      CobaltoRegal@mailbarn.net
    </p>
    <p class="contact-phone">555-271-6048</p>
  </div>
</div>
</body>
</html>
```